RM Skyline Imaging Web Site design

I am looking for a responsive single page website deign for rmskylineimages.com. This is a drone based aerial photography and cinematography business. It should have an about us section, a services section that contains photograph service, Video footage, and Aerial mapping all under the services section, a pricing section, and then a contact page for customers to contact us.

Coding

Coded - Design and coding required

Number of Pages Required

1 page

Font styles to use
Sans Serif

Colors

Designer to choose colors to be used in the design.

Requirements
Must have
• Responsive design. About us section, services section, pricing section under the services links, and contact us section, that links to a submission page where they can send Name, address, email, and comments on what they are interested in.
• See hoverlens7.com - looking for similar design.
Should not have
• clutter, or too busy design

```html
<!DOCTYPE html>
<html lang="en">
<head>
<meta charset="utf-8">
<title>RM Skyline Imaging – Drone Aerial Photography</title>
<link href="https://fonts.googleapis.com/css2?family=Lato:wght@400;700&family=Open+Sans:wght@400;600&display=swap" rel="stylesheet">
<style>
:root{
  --orange:#f7731b;
  --orange-deep:#ee5d0c;
  --charcoal:#2d2d2d;
  --card-dark:#333333;
  --ink:#1e1e1e;
  --muted:#6b6b6b;
  --white:#ffffff;
  --footer:#ececec;
  --field-border:#3c4a78;
}
*{box-sizing:border-box;margin:0;padding:0}
html,body{width:1200px;height:3136px;overflow:hidden}
body{position:relative;background:var(--white);font-family:"Open Sans",Arial,sans-serif;color:var(--ink)}
.abs{position:absolute}
.center{text-align:center}

/* hero */
.hero{left:0;top:0;width:1200px;height:710px;clip-path:polygon(0 0,100% 0,100% 638px,0 710px);
  background:linear-gradient(160deg,#4a4d52 0%,#2c2f33 45%,#3b3a38 75%,#24272a 100%)}
.brand{left:115px;top:34px;display:flex;align-items:center;gap:14px;color:var(--white);
  font-family:"Lato",Arial,sans-serif;font-size:26px;letter-spacing:4px}
.brand-dot{width:26px;height:26px;border-radius:50%;background:var(--orange)}
.nav{top:58px;right:125px;display:flex;gap:44px;font-family:"Lato",Arial,sans-serif;font-weight:700;font-size:15px;color:var(--white)}
.nav .active{color:var(--orange)}
.hero-title{left:0;top:278px;width:1200px;font-family:"Lato",Arial,sans-serif;font-size:40px;line-height:50px;color:var(--white);letter-spacing:1px}
.btn-outline-orange{left:505px;top:387px;width:192px;height:46px;border:3px solid var(--orange);color:var(--white);
  font-family:"Lato",Arial,sans-serif;font-weight:700;font-size:15px;line-height:40px;text-align:center}
.dots{left:556px;top:643px;display:flex;gap:10px}
.dots span{width:14px;height:14px;border-radius:50%;background:var(--white)}
.dots span:first-child{background:transparent;border:2px solid var(--white)}

/* about */
.about-mark{left:0;top:736px;width:1200px;display:flex;justify-content:center;align-items:center;gap:10px;
  font-family:"Lato",Arial,sans-serif;font-weight:700;font-size:18px;color:var(--charcoal)}
.about-mark .brand-dot{width:20px;height:20px}
.section-title{font-family:"Lato",Arial,sans-serif;font-weight:700;font-size:30px;letter-spacing:.5px}
.about-title{left:0;top:794px;width:1200px;color:var(--ink)}
.about-lead{left:180px;top:860px;width:840px;font-size:16px;line-height:26px;color:var(--muted)}
.about-body{left:180px;top:926px;width:840px;font-size:14px;line-height:26px;color:var(--muted)}
.video{top:1089px;width:442px;height:281px;border:3px solid #e2e2e2;box-shadow:0 0 0 1px #c9c9c9}
.video svg{display:block}

/* services */
.services{left:0;top:1404px;width:1200px;height:560px;clip-path:polygon(0 0,100% 69px,100% 100%,0 100%);
  background:linear-gradient(180deg,#3a3b3d,#2a2b2d)}
.services-title{left:0;top:1484px;width:1200px;color:var(--white);font-weight:400}
.service{top:1562px;width:300px;color:var(--white)}
.service h3{font-family:"Lato",Arial,sans-serif;font-weight:700;font-size:22px;margin-top:10px}
.service p{font-size:14px;line-height:22px;margin:6px auto 0;width:270px}
.btn-outline-white{display:inline-block;margin-top:20px;width:138px;height:32px;border:2px solid var(--white);
  font-family:"Lato",Arial,sans-serif;font-weight:700;font-size:11px;line-height:28px}

/* pricing */
.pricing{left:0;top:1908px;width:1200px;height:600px;clip-path:polygon(0 36px,100% 0,100% 600px,0 527px);
  background:linear-gradient(180deg,#fb7e24 0%,#f26a12 30%,#ee6614 70%,#f57a20 100%)}
.pricing-title{left:0;top:1960px;width:1200px;color:var(--white);font-weight:400}
.plan{background:var(--card-dark);color:var(--white);text-align:center;font-family:"Lato",Arial,sans-serif}
.plan-basic{left:200px;top:2042px;width:264px;height:341px}
.plan-premium{left:755px;top:2042px;width:265px;height:341px}
.plan-standard{left:464px;top:2019px;width:291px;height:385px;background:var(--white);color:var(--ink);box-shadow:0 4px 18px rgba(0,0,0,.3);z-index:2}
.plan h4{font-weight:700;font-size:17px;margin-top:24px}
.plan-standard h4{color:var(--orange);margin-top:26px}
.price{font-size:50px;margin-top:6px;line-height:60px}
.price sup{font-size:28px;vertical-align:18px}
.price small{font-size:26px}
.features{list-style:none;font-family:"Open Sans",Arial,sans-serif;font-size:13px;margin:12px 26px 0}
.features li{padding:10px 0;border-bottom:1px solid rgba(255,255,255,.25)}
.plan-standard .features li{border-bottom:1px solid #c9c9c9;padding:12px 0}
.features li:last-child{border-bottom:none}
.btn-orange{display:inline-block;margin-top:8px;width:144px;height:34px;background:var(--orange);color:var(--white);
  font-weight:700;font-size:15px;line-height:34px}
.plan-standard .btn-orange{width:152px;height:38px;line-height:38px;margin-top:12px}

/* contact */
.drone-photo{left:1010px;top:2508px;width:190px;height:300px;border-radius:40px 0 0 60px;
  background:linear-gradient(135deg,#f4f4f4,#d7d8da 60%,#bfc1c4)}
.contact-card{left:186px;top:2540px;width:830px;height:353px;background:var(--white);border-radius:6px;
  box-shadow:0 4px 24px rgba(0,0,0,.18)}
.contact-title{left:0;top:28px;width:830px;font-weight:400;font-size:28px}
.field-label{font-family:"Lato",Arial,sans-serif;font-weight:700;font-size:15px}
.field{border:2px solid var(--field-border);height:40px;font-size:12px;color:#9a9a9a;padding:10px 14px}
.btn-submit{left:516px;top:2872px;width:170px;height:42px;background:var(--orange);color:var(--white);
  font-family:"Lato",Arial,sans-serif;font-weight:700;font-size:17px;line-height:42px;text-align:center;z-index:3}

/* footer */
.footer{left:0;top:2978px;width:1200px;height:158px;background:var(--footer)}
.footer-nav{left:0;top:3014px;width:1200px;display:flex;justify-content:center;gap:44px;font-family:"Lato",Arial,sans-serif;font-weight:700;font-size:15px;color:var(--ink)}
.copyright{left:0;top:3046px;width:1200px;font-size:12px;color:var(--muted)}
.social{left:512px;top:3075px;display:flex;gap:10px}
.social span{width:34px;height:34px;border:2px solid var(--ink);border-radius:50%}
</style>
</head>
<body>

<!-- Hero -->
<div class="abs hero" role="img" aria-label="Top-down aerial photograph of city skyscrapers"></div>
<div class="abs brand"><span class="brand-dot"></span>RM Skyline Imaging</div>
<nav class="abs nav"><span class="active">HOME</span><span>ABOUT US</span><span>SERVICES</span><span>OUR WORK</span><span>CONTACT</span></nav>
<h1 class="abs hero-title center" style="font-weight:400">DRONE BASED AERIAL PHOTOGRAPHY<br>AND CINEMATOGRAPHY</h1>
<div class="abs btn-outline-orange">READ MORE</div>
<div class="abs dots"><span></span><span></span><span></span><span></span></div>

<!-- About -->
<div class="abs about-mark"><span class="brand-dot"></span>RM Skyline Imaging</div>
<h2 class="abs section-title about-title center">ABOUT AERIAL PHOTOGRAPHY</h2>
<p class="abs about-lead center">Mauris vel lacus vitae felis vestibulum volutpat Etiam est nunc venenatis in tristique eu imperdiet ac nisl Cum sociis natoque penatibus et magnis dis parturient montes nascetur ridiculus</p>
<p class="abs about-body center">Vivamus porttitor purus nisi eleifend libero a tempus libero lectus feugiat felis Morbi diam mauris viverra in gravida eu mattis in ante Morbi eget arcu Morbi porta libero id ullamcorper nonummy nibh ligula pulvinar metus eget consectetuer augue nisi quis lacus Ut ac mi quis lacus mollis aliquam Curabitur iaculis tempus eros Curabitur vel mi sit amet magna malesuada ultrices Ut nisi erat fermentum vel congue id euismod in elit Fusce ultricies orci ac</p>

<div class="abs video" style="left:142px">
  <svg width="436" height="275" viewBox="0 0 436 275">
    <rect width="436" height="275" fill="#2f4a25" role="img" aria-label="Aerial video still of a winding road through forest"/>
    <rect width="436" height="275" fill="url(#forest)"/>
    <defs><linearGradient id="forest" x1="0" y1="0" x2="1" y2="1"><stop offset="0" stop-color="#3d5f2c"/><stop offset="1" stop-color="#223a1a"/></linearGradient></defs>
    <circle cx="218" cy="137" r="38" fill="none" stroke="#fff" stroke-width="3"/>
    <path d="M208 118 L236 137 L208 156 Z" fill="none" stroke="#fff" stroke-width="3" stroke-linejoin="round"/>
  </svg>
</div>
<div class="abs video" style="left:622px">
  <svg width="436" height="275" viewBox="0 0 436 275">
    <defs><linearGradient id="city" x1="0" y1="0" x2="1" y2="1"><stop offset="0" stop-color="#4c5156"/><stop offset="1" stop-color="#2c3034"/></linearGradient></defs>
    <rect width="436" height="275" fill="url(#city)" role="img" aria-label="Aerial video still of a city roundabout"/>
    <circle cx="218" cy="137" r="38" fill="none" stroke="#fff" stroke-width="3"/>
    <path d="M208 118 L236 137 L208 156 Z" fill="none" stroke="#fff" stroke-width="3" stroke-linejoin="round"/>
  </svg>
</div>

<!-- Services -->
<div class="abs services" role="img" aria-label="Darkened aerial photograph of a city district"></div>
<h2 class="abs section-title services-title center">OUR SERVICES</h2>

<div class="abs service center" style="left:122px">
  <svg width="130" height="130" viewBox="0 0 130 130">
    <circle cx="65" cy="65" r="58" fill="none" stroke="#fff" stroke-width="8" stroke-dasharray="76 15"/>
    <rect x="35" y="45" width="60" height="40" fill="none" stroke="#fff" stroke-width="3"/>
    <line x1="35" y1="53" x2="95" y2="53" stroke="#fff" stroke-width="2"/>
    <line x1="35" y1="77" x2="95" y2="77" stroke="#fff" stroke-width="2"/>
    <path d="M59 57 L73 65 L59 73 Z" fill="none" stroke="#fff" stroke-width="2.5"/>
  </svg>
  <h3>Video Footage</h3>
  <p>Etiam est nunc venenatis in tristique eu imperdiet ac nisl Cum sociis natoque penatibus et magnis dis pa</p>
  <span class="btn-outline-white">READ MORE</span>
</div>

<div class="abs service center" style="left:450px">
  <svg width="130" height="130" viewBox="0 0 130 130">
    <circle cx="65" cy="65" r="58" fill="none" stroke="#fff" stroke-width="8" stroke-dasharray="76 15"/>
    <rect x="38" y="38" width="54" height="54" fill="none" stroke="#fff" stroke-width="3"/>
    <path d="M38 62 H92 M62 38 V92 M70 70 L92 92" stroke="#fff" stroke-width="2" fill="none"/>
    <circle cx="76" cy="52" r="6" fill="none" stroke="#fff" stroke-width="2.5"/>
  </svg>
  <h3>Aerial Mapping</h3>
  <p>Etiam est nunc venenatis in tristique eu imperdiet ac nisl Cum sociis natoque penatibus et magnis dis pa</p>
  <span class="btn-outline-white">READ MORE</span>
</div>

<div class="abs service center" style="left:776px">
  <svg width="130" height="130" viewBox="0 0 130 130">
    <circle cx="65" cy="65" r="58" fill="none" stroke="#fff" stroke-width="8" stroke-dasharray="76 15"/>
    <rect x="54" y="54" width="22" height="22" rx="4" fill="none" stroke="#fff" stroke-width="3"/>
    <path d="M54 54 L44 44 M76 54 L86 44 M54 76 L44 86 M76 76 L86 86" stroke="#fff" stroke-width="3"/>
    <circle cx="40" cy="40" r="9" fill="none" stroke="#fff" stroke-width="2.5"/>
    <circle cx="90" cy="40" r="9" fill="none" stroke="#fff" stroke-width="2.5"/>
    <circle cx="40" cy="90" r="9" fill="none" stroke="#fff" stroke-width="2.5"/>
    <circle cx="90" cy="90" r="9" fill="none" stroke="#fff" stroke-width="2.5"/>
  </svg>
  <h3>Photogarphy</h3>
  <p>Etiam est nunc venenatis in tristique eu imperdiet ac nisl Cum sociis natoque penatibus et magnis dis pa</p>
  <span class="btn-outline-white">READ MORE</span>
</div>

<!-- Pricing -->
<div class="abs pricing" role="img" aria-label="Orange-tinted aerial photograph of a town"></div>
<h2 class="abs section-title pricing-title center">OUR PRICING</h2>

<div class="abs plan plan-basic">
  <h4>BASIC</h4>
  <div class="price"><sup>$</sup>20<small>.00</small></div>
  <ul class="features"><li>Morbi diam mauris</li><li>Aiverra in gravida eu</li><li>Mattis in ante Morbi</li><li>Eget arcu Morbi</li></ul>
  <span class="btn-orange">CLICK HERE</span>
</div>
<div class="abs plan plan-standard">
  <h4>STANDARD</h4>
  <div class="price"><sup>$</sup>50<small>.00</small></div>
  <ul class="features"><li>Morbi diam mauris</li><li>Aiverra in gravida eu</li><li>Mattis in ante Morbi</li><li>Eget arcu Morbi</li></ul>
  <span class="btn-orange">CLICK HERE</span>
</div>
<div class="abs plan plan-premium">
  <h4>PREMIUM</h4>
  <div class="price"><sup>$</sup>75<small>.00</small></div>
  <ul class="features"><li>Morbi diam mauris</li><li>Aiverra in gravida eu</li><li>Mattis in ante Morbi</li><li>Eget arcu Morbi</li></ul>
  <span class="btn-orange">CLICK HERE</span>
</div>

<!-- Contact -->
<div class="abs drone-photo" role="img" aria-label="Photograph of a white camera drone"></div>
<section class="abs contact-card">
  <h2 class="abs section-title contact-title center">CONTACT US</h2>
  <span class="abs field-label" style="left:46px;top:100px">Name</span>
  <div class="abs field" style="left:46px;top:122px;width:238px">Name</div>
  <span class="abs field-label" style="left:298px;top:100px">Email</span>
  <div class="abs field" style="left:298px;top:122px;width:238px">Email</div>
  <span class="abs field-label" style="left:545px;top:100px">Address</span>
  <div class="abs field" style="left:545px;top:122px;width:238px">Address</div>
  <span class="abs field-label" style="left:46px;top:186px">Comment</span>
  <div class="abs field" style="left:46px;top:208px;width:737px;height:92px">Comment</div>
</section>
<div class="abs btn-submit">SUBMIT</div>

<!-- Footer -->
<footer class="abs footer"></footer>
<nav class="abs footer-nav"><span>HOME</span><span>ABOUT US</span><span>SERVICES</span><span>OUR WORK</span><span>CONTACT</span></nav>
<p class="abs copyright center">© 2017 Company Name. All right reserved</p>
<div class="abs social"><span></span><span></span><span></span><span></span></div>

</body>
</html>
```